PennacottHoldings.com Website Design

Simple website using existing logo. See "free website" already up. Want something much more professional and dynamic. Purpose is to describe my business and give me a place to post and update projects as they move along. Need to be able to post links to other companies that my firm invests equity in.
Target Market(s)
Banks, Financial Advisors
Industry/Entity Type
It Professional
Number of Pages Required
4 page
Font styles to use
Sans Serif
Requirements
Must have
- Ability to add and edit projects so they appear in the order of most current to oldest.
Nice to have
- Page to blog and link to facebook page

```html
<!DOCTYPE html>
<html lang="en">
<head>
<meta charset="utf-8">
<title>Pennacott Holdings</title>
<link href="https://fonts.googleapis.com/css2?family=Oswald:wght@400;500;600&family=Open+Sans:wght@400;600;700&display=swap" rel="stylesheet">
<style>
  :root{
    --red:#d3171c;
    --red-dark:#a90f13;
    --ink:#2b2b2b;
    --text:#5a5a5a;
    --muted:#9a9a9a;
    --light:#f1f1f1;
    --footer:#2f2f2f;
    --footer-deep:#1f1f1f;
    --white:#ffffff;
  }
  *{box-sizing:border-box;margin:0;padding:0}
  html,body{width:784px;height:1200px;overflow:hidden}
  body{font-family:"Open Sans",Arial,sans-serif;color:var(--text);background:var(--white);position:relative}
  .page{position:absolute;inset:0;width:784px;height:1200px}

  /* header */
  .site-header{position:absolute;top:0;left:0;width:784px;height:74px;border-top:4px solid var(--red)}
  .brand{position:absolute;left:72px;top:16px;display:flex;align-items:center;gap:10px}
  .brand-mark{width:38px;height:38px;background:var(--red)}
  .brand-name{font-family:"Oswald",sans-serif;font-weight:600;font-size:26px;color:var(--ink);letter-spacing:.5px}
  .social{position:absolute;right:72px;top:10px;display:flex;gap:6px}
  .social span{width:18px;height:18px;border-radius:50%;background:#9aa0a6}
  .phone{position:absolute;right:72px;top:36px;display:flex;align-items:center;gap:6px;font-family:"Oswald",sans-serif;font-weight:500;font-size:20px;color:var(--ink)}

  .main-nav{position:absolute;top:74px;left:72px;width:640px;height:24px;display:flex;font-size:11px;font-weight:600;color:var(--ink)}
  .main-nav a{color:inherit;text-decoration:none;padding:0 16px;line-height:24px}
  .main-nav a.active{background:var(--red);color:var(--white)}
  .main-nav .push{margin-left:auto}

  /* hero */
  .hero{position:absolute;top:98px;left:0;width:784px;height:268px;background:linear-gradient(90deg,#f6f6f6 0%,#e4e6e8 45%,#c9ccd0 70%,#eceef0 100%)}
  .hero-copy{position:absolute;left:40px;top:150px;width:440px}
  .hero-title{font-family:"Oswald",sans-serif;font-weight:500;font-size:22px;line-height:1.15;color:var(--white);background:var(--red);display:inline;padding:2px 6px;box-decoration-break:clone;-webkit-box-decoration-break:clone}
  .hero-sub{margin-top:8px;font-size:10px;color:var(--ink)}

  /* about */
  .about{position:absolute;top:366px;left:0;width:784px;height:170px;text-align:center}
  .section-title{font-family:"Oswald",sans-serif;font-weight:400;font-size:26px;color:var(--ink);margin-top:18px}
  .section-title .hl{color:var(--white)}
  .rule{width:640px;height:1px;background:#ddd;margin:6px auto 10px}
  .lead{font-size:9.5px;color:var(--red);margin:0 auto 2px;width:560px}
  .body-text{font-size:9.5px;line-height:1.5;width:560px;margin:0 auto}
  .btn{display:inline-block;background:var(--red);color:var(--white);font-size:9px;font-weight:700;padding:5px 11px;margin-top:8px;border-radius:2px}

  /* projects */
  .projects{position:absolute;top:548px;left:0;width:784px;height:222px;background:linear-gradient(180deg,var(--red) 0%,var(--red-dark) 100%)}
  .projects .section-title{text-align:center;color:var(--ink);margin-top:10px}
  .projects-copy{position:absolute;left:86px;top:70px;width:290px;color:var(--white);font-size:9.5px;line-height:1.55}
  .projects-copy .btn{background:var(--red-dark);border:1px solid rgba(255,255,255,.3)}
  .projects-visual{position:absolute;left:420px;top:58px;width:270px;height:160px;border-radius:10px;background:linear-gradient(135deg,#3a3a3a 0%,#bfc3c8 50%,#e8d8d2 100%)}

  /* services */
  .services{position:absolute;top:786px;left:86px;width:612px;height:220px;display:flex;gap:24px}
  .card{flex:1;background:var(--white);box-shadow:0 1px 4px rgba(0,0,0,.2);text-align:center;padding-bottom:10px}
  .card-visual{height:120px}
  .v1{background:linear-gradient(180deg,#d9d9d9,#7d7d7d)}
  .v2{background:linear-gradient(180deg,#c6c6c6,#5d5d5d)}
  .v3{background:linear-gradient(180deg,#efefef,#6b6b6b)}
  .card-title{font-family:"Oswald",sans-serif;font-weight:500;font-size:14px;color:var(--ink);background:var(--white);margin-top:-14px;display:inline-block;padding:2px 10px}
  .card p{font-size:9px;line-height:1.45;padding:4px 16px 0}

  /* footer */
  .site-footer{position:absolute;top:1022px;left:0;width:784px;height:150px;background:var(--footer);color:#cfcfcf}
  .footer-col{position:absolute;top:18px}
  .footer-col h3{font-family:"Oswald",sans-serif;font-weight:400;font-size:15px;color:var(--white);margin-bottom:10px}
  .links{display:flex;gap:40px;font-size:9px;line-height:1.9}
  .links ul{list-style:none}
  .links li::before{content:"› ";color:var(--muted)}
  .contact p{font-size:9px;line-height:1.9}
  .footer-brand{position:absolute;right:86px;top:48px;display:flex;align-items:center;gap:10px}
  .footer-brand .mark{width:36px;height:36px;background:#6a6a6a}
  .footer-brand .name{font-family:"Oswald",sans-serif;font-weight:600;font-size:24px;color:#7a7a7a}
  .bottom-bar{position:absolute;top:1172px;left:0;width:784px;height:28px;background:var(--footer-deep);font-size:9px;color:#aaa}
  .bottom-bar p{position:absolute;left:86px;top:8px}
  .bottom-bar .social{right:86px;top:5px}
  .bottom-bar .social span{background:#555}
</style>
</head>
<body>
<div class="page">
  <header class="site-header">
    <div class="brand"><span class="brand-mark"></span><span class="brand-name">Pennacott Holdings</span></div>
    <div class="social"><span></span><span></span><span></span><span></span><span></span><span></span></div>
    <div class="phone">
      <svg width="16" height="16" viewBox="0 0 24 24"><path fill="#2b2b2b" d="M6.6 10.8a15.1 15.1 0 0 0 6.6 6.6l2.2-2.2c.3-.3.7-.4 1-.2 1.1.4 2.3.6 3.6.6.6 0 1 .4 1 1V20c0 .6-.4 1-1 1A17 17 0 0 1 3 4c0-.6.4-1 1-1h3.5c.6 0 1 .4 1 1 0 1.3.2 2.5.6 3.6.1.3 0 .7-.2 1z"/></svg>
      555.014.2290
    </div>
  </header>

  <nav class="main-nav">
    <a class="active">Home</a>
    <a>About Pennacott</a>
    <a>Real estate</a>
    <a>Press Release</a>
    <a class="push">Services</a>
    <a>Blog</a>
    <a>Contact</a>
  </nav>

  <section class="hero" role="img" aria-label="Photo of business people in a meeting around a presentation board">
    <div class="hero-copy">
      <h1 class="hero-title">PENNACOTT HOLDINGS IS THE PRIVATE EQUITY SPINOFF OF THE PENNACOTT COMPANIES.</h1>
      <p class="hero-sub">A Premium Family-owned Real Estate Company based in Amarillo, Texas</p>
    </div>
  </section>

  <section class="about">
    <h2 class="section-title">About Pennacott</h2>
    <div class="rule"></div>
    <p class="lead">Long-term capital for family businesses and regional ventures across West Texas.</p>
    <p class="body-text">We invest private equity alongside seasoned operators, giving growing firms the capital, guidance and patience they need. Our team works closely with banks and financial advisors to structure deals that last, and we keep every partner informed as each project moves forward.</p>
    <span class="btn">Read More</span>
  </section>

  <section class="projects">
    <h2 class="section-title">Latest <span class="hl">Projects</span></h2>
    <div class="projects-copy">
      <p>Follow our current investments from first funding to completion. New projects appear at the top of the list, with progress notes, photos and links to the companies we support.</p>
      <span class="btn">Read More</span>
    </div>
    <div class="projects-visual" role="img" aria-label="Photo of hands holding a tablet showing a financial chart"></div>
  </section>

  <section class="services">
    <article class="card">
      <div class="card-visual v1" role="img" aria-label="Photo of two consultants talking at a desk"></div>
      <h3 class="card-title">BUSINESS CONSULTING</h3>
      <p>Practical guidance on strategy, structure and growth for owners.</p>
      <span class="btn">Read More</span>
    </article>
    <article class="card">
      <div class="card-visual v2" role="img" aria-label="Photo of a financial growth chart"></div>
      <h3 class="card-title">EQUITY CAPITAL</h3>
      <p>Equity partnerships that align our capital with your long-term goals.</p>
      <span class="btn">Read More</span>
    </article>
    <article class="card">
      <div class="card-visual v3" role="img" aria-label="Photo of climbers helping each other up a summit"></div>
      <h3 class="card-title">MENTORING</h3>
      <p>Hands-on mentoring for founders and leadership teams as they scale.</p>
      <span class="btn">Read More</span>
    </article>
  </section>

  <footer class="site-footer">
    <div class="footer-col" style="left:86px">
      <h3>Quick Links</h3>
      <div class="links">
        <ul><li>Home</li><li>About Pennacott</li><li>Real estate</li><li>Press Release</li></ul>
        <ul><li>Services</li><li>Blog</li><li>Contact Us</li></ul>
      </div>
    </div>
    <div class="footer-col contact" style="left:330px">
      <h3>Contact Detail</h3>
      <p>Evan Pennacott</p>
      <p>Founder, Pennacott Holdings</p>
      <p>555.014.2290</p>
      <p>info@pennacottholdings.com</p>
    </div>
    <div class="footer-brand"><span class="mark"></span><span class="name">Pennacott Holdings</span></div>
  </footer>
  <div class="bottom-bar">
    <p>© 2014 Pennacott Holdings. All rights reserved.</p>
    <div class="social"><span></span><span></span><span></span><span></span><span></span></div>
  </div>
</div>
</body>
</html>
```